Business Card for Quillmark Ledger - A cannabis publication for executives.

I'd like some business cards for Quillmark Ledger. The logo is done (great job!) and I need a card design I will use with PRINTLY. I made it a short project to allow time for printing before an event. These will be standard sized cards (final artwork size 3.66" x 2.16" at 300dpi) with a final card size of 3.5" x 2.0". (See PRINTLY.com if you need more info.) I might try rounded corners but am not sure yet. I think the design will work okay with rounded.

Quillmark Ledger will be a bi-weekly publication for the cannabis industry. It is targeted to investors and industry executives, not consumers or pot smokers. So our market is more B2B. However I am open to creativity and making the card something people remark on.

My contact for card:

Dana Merrow
Founder/CEO
dana@quillmarkledger.example

2740 Harlow Avenue
Boston MA 02135
(617)555-0194

Target Market(s)

Executives, Industry people and investors in the Cannabis sector.

Contact Information for Business Card

PRINTLY does do double sided and the second side can be the same or different images. Only one side is required but use of the second side would be a bonus.

Font styles to use
Serif
Sans Serif
Decorative

Colors

Designer to choose colors to be used in the design.

Requirements
Must have
• Logo, contact info
Nice to have
• Style and design to make the card stand out in a crowd.

```html
<!DOCTYPE html>
<html lang="en">
<head>
<meta charset="utf-8">
<title>Quillmark Ledger — Business Card</title>
<link href="https://fonts.googleapis.com/css2?family=Montserrat:wght@700&family=Open+Sans:wght@400;600&display=swap" rel="stylesheet">
<style>
  :root{
    --stage:#1e1f21;
    --card-dark:#4a4b4e;
    --card-dark-edge:#3c3d40;
    --card-light:#ffffff;
    --brand-blue:#1b74bb;
    --brand-green:#7ab42c;
    --ink:#5a5c60;
    --ink-soft:#6c6e72;
  }
  *{box-sizing:border-box;margin:0;padding:0}
  html,body{width:1200px;height:1000px;overflow:hidden;background:var(--stage)}
  .stage{position:relative;width:1200px;height:1000px}
  .card{
    position:absolute;width:620px;height:354px;border-radius:26px;
    box-shadow:0 14px 30px rgba(0,0,0,.45);overflow:hidden;
    font-family:"Open Sans",Arial,sans-serif;
  }
  .card--back{left:130px;top:90px;background:linear-gradient(160deg,var(--card-dark),var(--card-dark-edge))}
  .card--front{left:450px;top:530px;background:var(--card-light)}

  .wordmark{display:flex;align-items:center;gap:12px}
  .wordmark__square{width:30px;height:30px;background:var(--brand-green)}
  .wordmark__name{font-family:"Open Sans",Arial,sans-serif;font-weight:600;color:var(--brand-blue);white-space:nowrap}

  .card--back .wordmark{position:absolute;left:0;right:0;top:50%;transform:translateY(-50%);justify-content:center}
  .card--back .wordmark__name{font-size:34px}
  .card--back .wordmark__square{width:38px;height:38px}

  .card--front .wordmark{position:absolute;right:34px;top:118px}
  .card--front .wordmark__name{font-size:24px}

  .identity{position:absolute;left:38px;top:146px;padding-left:16px;border-left:5px solid var(--brand-blue)}
  .identity__name{font-family:"Montserrat",Arial,sans-serif;font-weight:700;font-size:27px;line-height:1.1}
  .identity__first{color:var(--brand-blue)}
  .identity__last{color:var(--brand-green)}
  .identity__title{font-size:15px;color:var(--ink);margin-top:3px}

  .address{position:absolute;left:58px;top:226px;display:flex;gap:8px;font-size:14px;line-height:1.3;color:var(--ink)}
  .address svg{flex:none;margin-top:2px}

  .contacts{position:absolute;left:38px;top:276px;padding-left:16px;border-left:5px solid var(--brand-green);list-style:none}
  .contacts li{display:flex;align-items:center;gap:10px;font-size:14px;line-height:1.35;color:var(--ink)}
  .contacts svg{flex:none}
  .contacts .accent{color:var(--brand-green)}
</style>
</head>
<body>
<main class="stage">

  <section class="card card--back" aria-label="Card back">
    <div class="wordmark">
      <span class="wordmark__square"></span>
      <span class="wordmark__name">Quillmark Ledger</span>
    </div>
  </section>

  <section class="card card--front" aria-label="Card front">
    <div class="wordmark">
      <span class="wordmark__square"></span>
      <span class="wordmark__name">Quillmark Ledger</span>
    </div>

    <div class="identity">
      <p class="identity__name"><span class="identity__first">Dana</span> <span class="identity__last">Merrow</span></p>
      <p class="identity__title">Founder/CEO</p>
    </div>

    <div class="address">
      <svg width="12" height="16" viewBox="0 0 12 16" aria-hidden="true"><path d="M6 0a6 6 0 0 0-6 6c0 4.5 6 10 6 10s6-5.5 6-10a6 6 0 0 0-6-6zm0 8.5A2.5 2.5 0 1 1 6 3.5a2.5 2.5 0 0 1 0 5z" fill="var(--brand-blue)"/></svg>
      <p>2740 Harlow Avenue<br>Boston MA 02135</p>
    </div>

    <ul class="contacts">
      <li>
        <svg width="13" height="13" viewBox="0 0 16 16" aria-hidden="true"><path d="M3.6 1 6 3.6 4.8 5.4c.9 2 2.6 3.7 4.6 4.6L11.2 8.8 14 11.2l-1.6 2.8C7 14 2 9 2 3.4z" fill="var(--brand-green)"/></svg>
        <span>(617)555-0194</span>
      </li>
      <li>
        <svg width="13" height="11" viewBox="0 0 16 12" aria-hidden="true"><rect width="16" height="12" rx="1" fill="var(--brand-green)"/><path d="M1 1l7 6 7-6" stroke="#fff" stroke-width="1.6" fill="none"/></svg>
        <span>dana@quillmarkledger.example</span>
      </li>
      <li>
        <svg width="13" height="13" viewBox="0 0 16 16" aria-hidden="true"><circle cx="9" cy="7" r="5" stroke="var(--brand-green)" stroke-width="2" fill="none"/><path d="M5.5 10.5 1.5 14.5" stroke="var(--brand-green)" stroke-width="2.4" stroke-linecap="round"/></svg>
        <span>www.<span class="accent">quillmarkledger</span>.example</span>
      </li>
    </ul>
  </section>

</main>
</body>
</html>
```